PPT Template for a company that develops software and intellectual property for use by accountants a

We are a boutique firm that develops specialised reporting applications, financial and non-financial reporting content, checklists and other intellectual property for use by business consultants and accounting firms in particular. The applications and content we are creating is strategically focussed and we are required to produce reports and presentations and our current templates are simply not sufficient.

Excel worksheets, graphs and other graphics are regularly embedded into the presentations
We have our logo in 4 colour palettes and will require the winning version to be provided in all 4 colours plus B&W. There is one single logo but the name “Lantern Trade Pathfinders” is presented in 3 different styles for use depending on the space available etc.
Our clients will typically take our products and rebrand/co brand these (we require them to at least say that there product is “powered by Lantern Trade Pathfinders” with the logo.
The templates you provide will be used to create marketing presentations, proposal presentations and our standard documents that clients will rebrand or cobrand under license.

A Powerpoint Document Slide Template

Cover page layout, back page, intermediate page heading, in colours and styles based on the logo, title styles, and an intermediate or chapter heading slide style. Many of our presentations contain slides with tables, diagrams, flowcharts and text, including simple lists of bullet points. As above, you will see in our style guide that we have four coloured logos – we would like one version in each. We recommend that we finalise the design using the maroon version and then this be used as the base for the other colour palettes.
Again, the cover should be bold and draw attention but remain professional.

We are looking for something that works in both 4:3 and 16:9 (or two templates please)

We like a clear professional and simple look.

Deliverable: PowerPoint template file (.potx extension) for PowerPoint 2007 with at least a “cover” layout, a “title and content” layout, and a simplified slide layout, as well as “back cover”. Please embed any fonts used.

Industry/Entity Type

Financial

```html
<!DOCTYPE html>
<html lang="en">
<head>
<meta charset="utf-8">
<title>Company Profile – Lantern Trade Pathfinders</title>
<link rel="stylesheet" href="https://fonts.googleapis.com/css2?family=Ubuntu:wght@500;700&family=Roboto:wght@400&family=Carlito:wght@700&display=swap">
<style>
  :root {
    --brand-red: #b01c22;
    --text-grey: #7a7a7a;
    --body-grey: #6f6f6f;
    --panel-grey: #ebebeb;
    --footer-grey: #808080;
    --rule-grey: #e6e6e6;
    --ink: #3a3a3a;
    --white: #ffffff;
  }
  * { margin: 0; padding: 0; box-sizing: border-box; }
  html, body { width: 1200px; height: 900px; overflow: hidden; background: var(--white); }
  .slide { position: relative; width: 1200px; height: 900px; background: var(--white); font-family: "Roboto", Arial, sans-serif; }

  .slide-header { position: absolute; left: 0; top: 0; width: 1200px; height: 108px; border-bottom: 2px solid var(--rule-grey); }
  .slide-title { position: absolute; left: 26px; top: 32px; font-family: "Ubuntu", Arial, sans-serif; font-weight: 700; font-size: 33px; color: var(--brand-red); letter-spacing: 0.2px; }
  .brand { position: absolute; right: 16px; top: 20px; display: flex; align-items: center; gap: 12px; }
  .brand-mark { width: 40px; height: 40px; background: var(--brand-red); }
  .brand-name { font-family: "Ubuntu", Arial, sans-serif; font-weight: 500; font-size: 17px; line-height: 19px; color: var(--ink); }

  .intro { position: absolute; left: 100px; top: 164px; width: 1020px; }
  .intro-heading { font-family: "Ubuntu", Arial, sans-serif; font-weight: 700; font-size: 22px; color: var(--brand-red); margin-left: 1px; }
  .intro-text { margin-top: 12px; margin-left: 10px; font-size: 18px; line-height: 25.5px; color: var(--text-grey); }

  .columns { position: absolute; left: 110px; top: 321px; display: flex; gap: 31px; }
  .column { width: 297px; height: 386px; background: var(--panel-grey); }
  .column-head { height: 56px; background: var(--brand-red); color: var(--white); font-family: "Carlito", Calibri, sans-serif; font-weight: 700; font-size: 27px; line-height: 56px; padding-left: 20px; }
  .column-body { padding: 20px 20px 0 19px; font-size: 18px; line-height: 28.5px; color: var(--body-grey); }

  .slide-footer { position: absolute; left: 0; bottom: 0; width: 1200px; height: 39px; background: var(--footer-grey); color: var(--white); font-family: "Roboto", Arial, sans-serif; font-size: 17px; line-height: 39px; display: flex; justify-content: space-between; padding: 0 15px 0 16px; }
</style>
</head>
<body>
<div class="slide">
  <header class="slide-header">
    <h1 class="slide-title">COMPANY PROFILE</h1>
    <div class="brand">
      <div class="brand-mark"></div>
      <div class="brand-name">Lantern<br>Trade<br>Pathfinders</div>
    </div>
  </header>

  <section class="intro">
    <h2 class="intro-heading">Table Head Here</h2>
    <p class="intro-text">Lorem ipsum dolor sit Lorem ipsum dolor sit&nbsp; Lorem ipsum dolor sit Lorem ipsum dolor sit&nbsp; Lorem ipsum dolor sit Lorem ipsum dolor&nbsp; Lorem ipsum dolor sit Lorem ipsum dolor sit&nbsp; Lorem ipsum dolor sit Lorem ipsum dolor sit&nbsp; Lorem ipsum dolor sit Lorem ipsum dolor&nbsp; Lorem ipsum dolor sit Lorem ipsum dolor sit&nbsp; Lorem ipsum dolor sit Lorem ipsum dolor sit</p>
  </section>

  <section class="columns">
    <article class="column">
      <h3 class="column-head">COL HEAD HERE</h3>
      <p class="column-body">Lorem ipsum dolor sit Lorem ipsum dolor sit&nbsp; Lorem ipsum dolor sit Lorem ipsum dolor Lorem ipsum dolor sit Lorem ipsum dolor sit&nbsp; Lorem ipsum dolor sit Lorem ipsum dolor sit Lorem ipsum dolor sit Lorem ipsum dolor sit&nbsp; Lorem ipsum dolor sit Lorem ipsum dolor Lorem ipsum dolor sit</p>
    </article>
    <article class="column">
      <h3 class="column-head">COL HEAD HERE</h3>
      <p class="column-body">Lorem ipsum dolor sit Lorem ipsum dolor sit&nbsp; Lorem ipsum dolor sit Lorem ipsum dolor Lorem ipsum dolor sit Lorem ipsum dolor sit&nbsp; Lorem ipsum dolor sit Lorem ipsum dolor sit Lorem ipsum dolor sit Lorem ipsum dolor sit&nbsp; Lorem ipsum dolor sit Lorem ipsum dolor Lorem ipsum dolor sit</p>
    </article>
    <article class="column">
      <h3 class="column-head">COL HEAD HERE</h3>
      <p class="column-body">Lorem ipsum dolor sit Lorem ipsum dolor sit&nbsp; Lorem ipsum dolor sit Lorem ipsum dolor Lorem ipsum dolor sit Lorem ipsum dolor sit&nbsp; Lorem ipsum dolor sit Lorem ipsum dolor sit Lorem ipsum dolor sit Lorem ipsum dolor sit&nbsp; Lorem ipsum dolor sit Lorem ipsum dolor Lorem ipsum dolor sit</p>
    </article>
  </section>

  <footer class="slide-footer">
    <span class="footer-credit">Powered By : Lantern Trade Pathfinders.</span>
    <span class="footer-copyright">Copyrighte@2014</span>
  </footer>
</div>
</body>
</html>
```